Design our branded business card!

We'd love for you to design our business card and come up with a fitting design that reflects the Brimble brand. We're a growing tech startup with big ambitions. We've included our brand guidelines (contain colour palette), logo (EPS vector in CMYK) and old designs to help you on your way.

We'd like to keep the design fairly simple:

* Name
* Phone number
* Email address
* Website (www.brimble.life)
* Twitter (@brimble)
* Address (19 Fenwick Row, Leeds, UK, LS4 9QT).

This would need to include print and cutting marks.

If you have any questions just let us know!

Target Market(s)

Businesses, Press and our customers!

Industry/Entity Type

Business

Contact Information for Business Card

* Name
* Phone number
* Email address
* Twitter (@brimble)

Font styles to use
Sans Serif

Requirements
Must have
• 1. Must have the Brimble logo included.
• 2. Must use the font 'Brandon Text' in either 'light' or 'thin' (https://www.typevaultex.com/fonts/qrnfoundry/brandon-text/)
• 3. Must use exact colours references from the brand guidelines. Colours outside of the brand guidelines will be discounted. White (transparent) backgrounds are fine.
• 4. Must contain the following information:
• * Name
• * Phone number
• * Email address
• * Website (www.brimble.life)
• * Twitter (@brimble)
• * Address (19 Fenwick Row, Leeds, UK, LS4 9QT).
Nice to have
• Must use the font 'Brandon Text' in either 'light' or 'thin' (https://www.typevaultex.com/fonts/qrnfoundry/brandon-text/)
Should not have
• Colours outside of the brand guidelines will be discounted. White (transparent) backgrounds are fine.
• Avoid creating icons or including photography.

```html
<!DOCTYPE html>
<html lang="en">
<head>
<meta charset="utf-8">
<title>Brimble business card</title>
<link rel="stylesheet" href="https://fonts.googleapis.com/css2?family=Lato:wght@300;400;700&display=swap">
<style>
  :root {
    --slate: #3c4446;
    --slate-light: #59636a;
    --paper: #ffffff;
    --green: #7cc36a;
    --green-dark: #5fae52;
    --ink: #4a5153;
    --ink-soft: #6b7275;
    --backdrop: #e8e5e0;
  }
  * { margin: 0; padding: 0; box-sizing: border-box; }
  html, body { width: 1200px; height: 1062px; overflow: hidden; }
  body {
    background: var(--backdrop);
    font-family: "Lato", sans-serif;
    position: relative;
  }
  .card {
    position: absolute;
    width: 640px;
    height: 366px;
    border-radius: 4px;
    overflow: hidden;
    box-shadow: 0 10px 28px rgba(0,0,0,.22);
  }
  .card-front { left: 90px; top: 110px; background: var(--slate); }
  .card-back {
    left: 470px; top: 586px;
    background: linear-gradient(135deg, var(--slate) 0%, var(--slate-light) 50%, var(--slate) 100%);
  }
  .card-shape { position: absolute; inset: 0; }

  .brand { position: absolute; display: flex; align-items: center; }
  .brand-dot { border-radius: 50%; background: var(--green); flex: none; }
  .brand-name { font-weight: 300; line-height: 1; letter-spacing: 1px; }

  .card-front .brand { left: 78px; top: 62px; gap: 18px; }
  .card-front .brand-dot { width: 62px; height: 62px; }
  .card-front .brand-name { font-size: 66px; color: var(--ink); }

  .holder { position: absolute; left: 80px; top: 160px; }
  .holder-name { font-size: 25px; font-weight: 700; color: var(--green); }
  .holder-role { font-size: 18px; font-weight: 400; color: var(--ink-soft); margin-top: 2px; }

  .contacts { position: absolute; left: 80px; top: 228px; list-style: none; }
  .contacts li {
    display: flex; align-items: center; gap: 10px;
    font-size: 15px; color: var(--ink); line-height: 24px;
  }
  .contacts svg, .address svg { width: 13px; height: 13px; flex: none; }

  .address {
    position: absolute; left: 392px; top: 176px;
    display: flex; gap: 10px; align-items: flex-start;
    font-size: 16px; color: var(--ink); line-height: 24px;
  }
  .address svg { margin-top: 5px; }

  .card-back .brand { left: 70px; top: 118px; gap: 28px; }
  .card-back .brand-dot { width: 120px; height: 120px; }
  .card-back .brand-name { font-size: 112px; color: var(--paper); }
</style>
</head>
<body>

<section class="card card-front" aria-label="Business card, front">
  <svg class="card-shape" viewBox="0 0 640 366" preserveAspectRatio="none" aria-hidden="true">
    <ellipse cx="320" cy="183" rx="318" ry="262" fill="none" stroke="var(--green)" stroke-width="6"/>
    <ellipse cx="320" cy="183" rx="302" ry="262" fill="var(--paper)"/>
  </svg>

  <div class="brand">
    <span class="brand-dot"></span>
    <span class="brand-name">brimble</span>
  </div>

  <div class="holder">
    <p class="holder-name">Daniel Hart</p>
    <p class="holder-role">Manager</p>
  </div>

  <ul class="contacts">
    <li>
      <svg viewBox="0 0 16 16"><path d="M4 1l3 3-2 2c1 2 3 4 5 5l2-2 3 3-2 3C7 15 1 9 1 3z" fill="var(--green)"/></svg>
      0113 496 0825
    </li>
    <li>
      <svg viewBox="0 0 16 16"><circle cx="8" cy="8" r="7" fill="none" stroke="var(--green)" stroke-width="1.6"/><path d="M1 8h14M8 1c-3 4-3 10 0 14M8 1c3 4 3 10 0 14" fill="none" stroke="var(--green)" stroke-width="1.2"/></svg>
      www.brimble.life
    </li>
    <li>
      <svg viewBox="0 0 16 16"><circle cx="8" cy="8" r="3" fill="none" stroke="var(--green)" stroke-width="1.8"/><path d="M11 5v4c0 2 3 2 3-1A6 6 0 1 0 11 13" fill="none" stroke="var(--green)" stroke-width="1.8"/></svg>
      d.hart@brimble.life
    </li>
    <li>
      <svg viewBox="0 0 16 16"><circle cx="8" cy="8" r="6" fill="var(--green)"/></svg>
      @brimble
    </li>
  </ul>

  <div class="address">
    <svg viewBox="0 0 16 16"><path d="M8 1a5 5 0 0 0-5 5c0 4 5 9 5 9s5-5 5-9a5 5 0 0 0-5-5z" fill="var(--green)"/><circle cx="8" cy="6" r="2" fill="var(--paper)"/></svg>
    <p>19 Fenwick Row, Leeds,<br>UK, LS4 9QT</p>
  </div>
</section>

<section class="card card-back" aria-label="Business card, back">
  <div class="brand">
    <span class="brand-dot"></span>
    <span class="brand-name">brimble</span>
  </div>
</section>

</body>
</html>
```